Harbor Business Cards

I need a business card designed with the following information.

Company Name: Harbor Wealth Management
Name: BriAnne Dockery
Title: Executive Assistant
Cell: (281) 555-0173
Direct Line: (832) 555-0148
Email: brianne@harborwmx.com
Address: 20537 W. Marlowe PKWY Ste. B
Tomball, TX 77390

I have attached the logo.
I would like it in navy blue and silver.
Thanks.

```html
<!DOCTYPE html>
<html lang="en">
<head>
<meta charset="utf-8">
<title>Harbor Wealth Management – Business Card</title>
<link rel="stylesheet" href="https://fonts.googleapis.com/css2?family=Cormorant+Garamond:wght@500&family=Open+Sans:wght@400;700&display=swap">
<style>
  :root {
    --navy: #13284d;
    --silver-light: #f1f1f1;
    --silver-mid: #c9c9c9;
    --silver-dark: #a9a9a9;
    --white: #ffffff;
    --backdrop: #2b2b2b;
  }
  * { box-sizing: border-box; margin: 0; padding: 0; }
  html, body {
    width: 1200px;
    height: 885px;
    overflow: hidden;
    background: var(--backdrop);
  }
  .canvas {
    position: relative;
    width: 1200px;
    height: 885px;
  }
  .card {
    position: absolute;
    width: 600px;
    height: 343px;
    overflow: hidden;
  }

  /* Front: silver */
  .card--front {
    left: 110px;
    top: 80px;
    background: linear-gradient(160deg, var(--silver-light) 0%, var(--silver-mid) 55%, var(--silver-dark) 100%);
  }
  .brand-name {
    font-family: "Cormorant Garamond", serif;
    font-weight: 500;
    color: var(--navy);
    text-transform: uppercase;
    letter-spacing: 0.32em;
    text-align: center;
    line-height: 1.35;
    font-size: 20px;
  }
  .card--front .brand-name {
    position: absolute;
    left: 0; right: 0;
    top: 120px;
  }
  .website {
    position: absolute;
    left: 0; right: 0;
    bottom: 46px;
    text-align: center;
    font-family: "Open Sans", sans-serif;
    font-size: 15px;
    letter-spacing: 0.28em;
    color: var(--white);
  }

  /* Back: white + navy */
  .card--back {
    left: 490px;
    top: 462px;
    background: var(--white);
    display: flex;
  }
  .brand-panel {
    width: 270px;
    height: 100%;
    display: flex;
    flex-direction: column;
    align-items: center;
    justify-content: center;
    gap: 22px;
  }
  .brand-mark {
    width: 34px;
    height: 34px;
    background: var(--navy);
  }
  .card--back .brand-name { font-size: 18px; }
  .stripes { width: 34px; height: 100%; display: block; }
  .contact-panel {
    flex: 1;
    background: var(--navy);
    color: var(--white);
    font-family: "Open Sans", sans-serif;
    text-align: right;
    padding: 28px 26px 0 0;
  }
  .person-name {
    font-weight: 700;
    font-size: 19px;
    text-transform: uppercase;
    line-height: 1.1;
  }
  .person-title {
    font-size: 14px;
    margin-bottom: 50px;
  }
  .contact-list { list-style: none; font-size: 13.5px; line-height: 1.45; }
  .contact-list li { display: flex; justify-content: flex-end; align-items: center; gap: 8px; }
  .contact-list .no-icon { padding-right: 20px; }
  .contact-list .email { margin-top: 18px; padding-right: 0; }
  .icon { width: 12px; height: 12px; flex: none; }
</style>
</head>
<body>
<main class="canvas">

  <section class="card card--front" aria-label="Card front">
    <p class="brand-name">Harbor<br>Wealth Management</p>
    <p class="website">www.harborwmx.com</p>
  </section>

  <section class="card card--back" aria-label="Card back">
    <div class="brand-panel">
      <span class="brand-mark" aria-hidden="true"></span>
      <p class="brand-name">Harbor<br>Wealth Management</p>
    </div>

    <svg class="stripes" viewBox="0 0 34 343" preserveAspectRatio="none" aria-hidden="true">
      <rect width="34" height="343" fill="var(--navy)"/>
      <rect x="0" width="5" height="343" fill="var(--white)"/>
      <rect x="9" width="3" height="343" fill="var(--white)"/>
      <rect x="16" width="3" height="343" fill="var(--white)"/>
      <rect x="23" width="3" height="343" fill="var(--white)"/>
    </svg>

    <div class="contact-panel">
      <p class="person-name">BriAnne Dockery</p>
      <p class="person-title">Executive Assistant</p>
      <ul class="contact-list">
        <li class="no-icon">20537 W. Marlowe PKWY Ste. B</li>
        <li>Tomball, TX 77390
          <svg class="icon" viewBox="0 0 12 12" aria-label="Direct line"><path d="M1 4 Q6 0 11 4 L10 5.5 L8 5 L8 4 Q6 3 4 4 L4 5 L2 5.5 Z M3 6 H9 L10 11 H2 Z" fill="var(--white)"/></svg>
        </li>
        <li>(832) 555-0148
          <svg class="icon" viewBox="0 0 12 12" aria-label="Cell"><rect x="3" y="0.5" width="6" height="11" rx="1" fill="none" stroke="var(--white)" stroke-width="1.2"/><circle cx="6" cy="9.5" r="0.7" fill="var(--white)"/></svg>
        </li>
        <li>(281) 555-0173
          <svg class="icon" viewBox="0 0 12 12" aria-label="Email"><rect x="0.5" y="2.5" width="11" height="7.5" fill="var(--white)"/><path d="M0.5 2.5 L6 7 L11.5 2.5" fill="none" stroke="var(--navy)" stroke-width="1"/></svg>
        </li>
        <li class="email">brianne@harborwmx.com</li>
      </ul>
    </div>
  </section>

</main>
</body>
</html>
```